Business card design for event company

need design double sided in square shape ( approx 6x6cm) in matt grey shades
front side :
logo ( could be in one color like picture attached ) printpress effect in a rect box

back side :
name in big font with silver foil finish ( similar to attached pic )

phone number i would like to see how it will look like if embossed ( like in credit cards )

Sample for contact on card ( will need 5 different contacts) - pls. include small icons next to each contact

KARIM SALEHI
Managing Director

+971 50 374 6619
karim@novlinkuae.com
www.novlink.ae
Building C2 , Office 318
Marsa Tirel Park

Please consider this is an urgent project . thank you in advance

```html
<!DOCTYPE html>
<html lang="en">
<head>
<meta charset="utf-8">
<title>Novlink business card</title>
<link href="https://fonts.googleapis.com/css2?family=Work+Sans:wght@400;500&display=swap" rel="stylesheet">
<style>
  :root {
    --backdrop: #1c1c1d;
    --card: #111112;
    --card-edge: #1f1f21;
    --silver: #d9d9da;
    --silver-soft: #b4b4b6;
    --emboss: #2c2c2e;
    --rule: #5a5a5c;
  }
  * { margin: 0; padding: 0; box-sizing: border-box; }
  html, body {
    width: 1200px;
    height: 900px;
    overflow: hidden;
    background: var(--backdrop);
    font-family: "Work Sans", Arial, sans-serif;
  }
  .canvas {
    position: relative;
    width: 1200px;
    height: 900px;
  }
  .card {
    position: absolute;
    left: 400px;
    width: 400px;
    height: 400px;
    background: linear-gradient(160deg, #171718 0%, var(--card) 60%, #0d0d0e 100%);
    border: 1px solid var(--card-edge);
  }
  .card--front { top: 35px; }
  .card--back { top: 465px; }

  .brand {
    position: absolute;
    display: flex;
    align-items: center;
    font-weight: 500;
    line-height: 1;
    white-space: nowrap;
  }
  .brand__square { display: block; flex: none; }

  .card--front .brand {
    left: 50%;
    top: 50%;
    transform: translate(-50%, -50%);
    gap: 12px;
    font-size: 52px;
    color: var(--silver);
  }
  .card--front .brand__square {
    width: 18px;
    height: 18px;
    background: var(--silver);
  }

  .card--back .brand {
    left: 22px;
    top: 50%;
    transform: translateY(-50%);
    gap: 7px;
    font-size: 26px;
    color: var(--emboss);
  }
  .card--back .brand__square {
    width: 9px;
    height: 9px;
    background: var(--emboss);
  }

  .divider {
    position: absolute;
    left: 150px;
    top: 80px;
    width: 1px;
    height: 240px;
    background: var(--rule);
  }
  .contact {
    position: absolute;
    left: 168px;
    top: 112px;
    color: var(--silver-soft);
  }
  .contact__name {
    font-size: 19px;
    font-weight: 500;
    letter-spacing: 1.2px;
    color: var(--silver);
  }
  .contact__role {
    font-size: 11px;
    letter-spacing: 0.5px;
    margin-top: 2px;
  }
  .contact__address {
    font-size: 12px;
    line-height: 16px;
    letter-spacing: 0.4px;
    margin-top: 16px;
  }
  .contact__list {
    list-style: none;
    margin-top: 8px;
  }
  .contact__item {
    display: flex;
    align-items: center;
    gap: 8px;
    font-size: 12px;
    line-height: 19px;
    letter-spacing: 0.4px;
  }
  .contact__item--phone {
    color: var(--silver);
    font-weight: 500;
    text-shadow: -1px -1px 0 rgba(255, 255, 255, 0.22), 1px 1px 1px #000;
  }
  .contact__icon {
    width: 9px;
    height: 9px;
    flex: none;
    fill: none;
    stroke: var(--silver-soft);
    stroke-width: 1.4;
  }
</style>
</head>
<body>
<main class="canvas">
  <section class="card card--front" aria-label="Card front">
    <div class="brand"><span class="brand__square"></span>Novlink</div>
  </section>

  <section class="card card--back" aria-label="Card back">
    <div class="brand"><span class="brand__square"></span>Novlink</div>
    <div class="divider"></div>
    <div class="contact">
      <h1 class="contact__name">KARIM SALEHI</h1>
      <p class="contact__role">Managing Director</p>
      <p class="contact__address">Building C2 , Office 318<br>Marsa Tirel Park</p>
      <ul class="contact__list">
        <li class="contact__item contact__item--phone">
          <svg class="contact__icon" viewBox="0 0 10 10"><path d="M2 1 L3.5 1 L4 3 L3 3.8 Q4 6 6.2 7 L7 6 L9 6.5 L9 8 Q5 9 2.5 6.5 Q1 4.5 2 1 Z"/></svg>
          +971 50 374 6619
        </li>
        <li class="contact__item">
          <svg class="contact__icon" viewBox="0 0 10 10"><rect x="1" y="2" width="8" height="6"/><path d="M1 2 L5 5.5 L9 2"/></svg>
          karim@novlinkuae.com
        </li>
        <li class="contact__item">
          <svg class="contact__icon" viewBox="0 0 10 10"><circle cx="5" cy="5" r="4"/><ellipse cx="5" cy="5" rx="1.8" ry="4"/><path d="M1 5 H9"/></svg>
          www.novlink.ae
        </li>
      </ul>
    </div>
  </section>
</main>
</body>
</html>
```